Webseite Toilettenvermietung
Zielgruppe
Wir vermieten mobile Toilettenkabine und Toilettenwagen. Wir haben noch eine Webseite kabinenpark-nord.de und lokus-verleihhaus.de und benötigen noch eine weitere. Es sollen nur die Miettoiletten und Toilettenwagen beworben werden
Aufgabenstellung
saubere und aussageräftige, farbliches Erscheinungsbild der Startseite.

```html
<!DOCTYPE html>
<html lang="de">
<head>
<meta charset="utf-8">
<title>Frischort – Mobile WC Mietservice</title>
<link href="https://fonts.googleapis.com/css2?family=Roboto+Condensed:wght@300;400&family=Roboto:wght@300;400&display=swap" rel="stylesheet">
<style>
  :root {
    --blue: #2d6db3;
    --brand: #1f63b5;
    --green: #8ab41b;
    --orange: #f07a1c;
    --grey-line: #cfcfcf;
    --text-dark: #2b2b2b;
    --text-grey: #8a8a8a;
    --nav-grey: #8c8c8c;
    --divider: #ececec;
    --navy: #2f3590;
  }
  * { box-sizing: border-box; margin: 0; padding: 0; }
  html, body { width: 1060px; height: 1200px; overflow: hidden; background: #fff; }
  body { position: relative; font-family: "Roboto", sans-serif; }

  .site-header {
    position: absolute; left: 0; top: 0; width: 1060px; height: 50px;
    background: linear-gradient(#ffffff, #efefef);
  }
  .brand {
    position: absolute; left: 265px; top: 10px; display: flex; align-items: center; gap: 7px;
    font-family: "Roboto Condensed", sans-serif; font-weight: 400; font-size: 22px; color: var(--brand);
  }
  .brand-dot { width: 14px; height: 14px; border-radius: 50%; background: var(--brand); }
  .main-nav { position: absolute; left: 461px; top: 0; height: 50px; display: flex; }
  .main-nav a {
    display: flex; align-items: center; justify-content: center; height: 50px;
    font-size: 7.5px; font-weight: 300; letter-spacing: .2px; color: var(--nav-grey); text-decoration: none;
    border-left: 1px solid #e2e2e2; border-bottom: 2px solid var(--grey-line);
  }
  .main-nav a:last-child { border-right: 1px solid #e2e2e2; }
  .main-nav .is-active { color: var(--blue); border-bottom-color: var(--blue); }
  .main-nav .nav-green { border-bottom-color: var(--green); }
  .main-nav .nav-orange { border-bottom-color: var(--orange); }

  .hero {
    position: absolute; left: 265px; top: 50px; width: 530px; height: 248px; overflow: hidden;
    background:
      radial-gradient(ellipse 90px 60px at 80% 12%, rgba(120,210,230,.45), transparent 70%),
      radial-gradient(ellipse 160px 120px at 62% 40%, rgba(205,140,120,.55), transparent 70%),
      radial-gradient(ellipse 140px 90px at 30% 35%, rgba(170,120,255,.55), transparent 70%),
      radial-gradient(ellipse 120px 80px at 88% 55%, rgba(200,150,255,.45), transparent 70%),
      linear-gradient(to bottom, rgba(0,0,0,0) 55%, rgba(25,15,45,.85) 100%),
      linear-gradient(135deg, #2a2f7a 0%, #4b3aa3 45%, #3a2a86 75%, #241c55 100%);
  }
  .hero-title {
    position: absolute; left: 21px; top: 68px; font-weight: 400;
    font-size: 28px; color: #fff; letter-spacing: .3px;
  }
  .hero-text { position: absolute; left: 24px; top: 103px; width: 210px; font-size: 7.5px; line-height: 9.2px; color: #fff; }
  .hero-button {
    position: absolute; left: 24px; top: 141px; width: 127px; height: 25px; background: var(--green);
    color: #fff; font-size: 9.5px; font-weight: 300; display: flex; align-items: center; justify-content: center;
  }
  .hero-dots { position: absolute; right: 10px; bottom: 4px; display: flex; gap: 3px; }
  .hero-dots span { width: 5px; height: 5px; border-radius: 50%; background: rgba(255,255,255,.55); }
  .hero-dots span:first-child { background: #fff; }

  .welcome {
    position: absolute; left: 265px; top: 325px; width: 530px; text-align: center;
    font-family: "Roboto Condensed", sans-serif; font-weight: 300; font-size: 17px; line-height: 20px; color: var(--blue);
  }

  .offer-title {
    position: absolute; font-family: "Roboto Condensed", sans-serif; font-weight: 300;
    font-size: 16.5px; color: var(--text-dark); white-space: nowrap;
  }
  .offer-text { position: absolute; width: 278px; font-weight: 300; font-size: 8.4px; line-height: 10.8px; color: var(--text-grey); }
  .details-button {
    position: absolute; width: 85px; height: 23px; border: 1px solid var(--blue); border-radius: 12px;
    color: var(--blue); font-size: 10px; font-weight: 300; display: flex; align-items: center; padding-left: 11px;
  }
  .details-button svg { position: absolute; right: 7px; top: 6px; }
  .divider { position: absolute; left: 265px; width: 530px; height: 1px; background: var(--divider); }

  .product-image { position: absolute; }
  .product-cabin {
    left: 622px; top: 398px; width: 145px; height: 152px; border-radius: 40px 40px 3px 3px;
    background: linear-gradient(100deg, #6c727a 0%, #8b9199 35%, #5c6168 55%, #7a8088 80%, #646a71 100%);
    box-shadow: 0 14px 18px -8px rgba(0,0,0,.25);
  }
  .product-container {
    left: 271px; top: 589px; width: 204px; height: 141px;
    background: linear-gradient(90deg, #d2d2d2 0%, #e0e0e0 44%, #f0f0f0 45%, #e6e6e6 100%);
    border: 5px solid var(--navy); border-right-width: 3px;
    box-shadow: 0 6px 10px -4px rgba(0,0,0,.2);
  }
  .product-wagon {
    left: 575px; top: 806px; width: 217px; height: 106px; border-radius: 3px;
    background: linear-gradient(#f6f6f6 0%, #e4e6ea 68%, #3a3f9a 74%, #2f3590 90%, rgba(47,53,144,0) 100%);
  }
  .product-toilet {
    left: 310px; top: 973px; width: 108px; height: 168px; border-radius: 22px 22px 2px 2px;
    background: linear-gradient(90deg, #6d7278 0%, #9ba0a5 30%, #a9adb2 55%, #82878c 100%);
    box-shadow: 0 8px 0 -2px #2a2a2a;
  }

  .site-footer { position: absolute; left: 271px; top: 1177px; display: flex; gap: 7px; }
  .site-footer span { font-family: "Roboto Condensed", sans-serif; font-weight: 300; font-size: 7px; color: var(--nav-grey); }
</style>
</head>
<body>
  <header class="site-header">
    <div class="brand"><span class="brand-dot"></span>Frischort</div>
    <nav class="main-nav">
      <a class="is-active" style="width:83px">STARTSEITE</a>
      <a class="nav-green" style="width:92px">MIETTOILETTEN</a>
      <a class="nav-orange" style="width:97px">TOILETTENWAGEN</a>
      <a style="width:62px">KONTAKT</a>
    </nav>
  </header>

  <section class="hero" role="img" aria-label="Konzertfoto: jubelnde Menge vor einer beleuchteten Bühne">
    <h1 class="hero-title">KOMMSTE MIT?</h1>
    <p class="hero-text">Lorem Ipsum is simply dummy text of the printing and typesetting industry. Lorem Ipsum has been the industry's standard dummy text ever since the 1500s....</p>
    <div class="hero-button">CONTACT US</div>
    <div class="hero-dots"><span></span><span></span><span></span></div>
  </section>

  <h2 class="welcome">WILLKOMMEN BEI FRISCHORT, IHR WC MIETSERVICE FÜR MOBILE<br>WC KABINEN, WAGEN &amp; CONTAINER</h2>

  <h3 class="offer-title" style="left:270px;top:438px">MOBILE WC KABINEN MIETEN</h3>
  <p class="offer-text" style="left:270px;top:466px">Unsere WC-Kabinen zum mieten bzw im Verleih. Hier finden Sie unsere Toilettenkabinen wie z. B. das mobile Baustellen WC, unser Universal Miete WC oder den Urinalstand in der Übersicht.</p>
  <div class="details-button" style="left:270px;top:516px">DETAILS<svg width="10" height="10" viewBox="0 0 10 10"><path d="M0 5h9M5 1l4 4-4 4" fill="none" stroke="#2d6db3" stroke-width="1"/></svg></div>
  <div class="product-image product-cabin" role="img" aria-label="Foto einer grauen mobilen WC-Kabine mit offener Tür"></div>
  <div class="divider" style="top:574px"></div>

  <div class="product-image product-container" role="img" aria-label="Foto eines weißen WC-Containers mit blauem Rahmen"></div>
  <h3 class="offer-title" style="left:508px;top:636px">MOBILE WC CONTAINER MIETEN</h3>
  <p class="offer-text" style="left:508px;top:664px">Unsere WC-Kabinen zum mieten bzw im Verleih. Hier finden Sie unsere Toilettenkabinen wie z. B. das mobile Baustellen WC, unser Universal Miete WC oder den Urinalstand in der Übersicht.</p>
  <div class="details-button" style="left:506px;top:708px">DETAILS<svg width="10" height="10" viewBox="0 0 10 10"><path d="M0 5h9M5 1l4 4-4 4" fill="none" stroke="#2d6db3" stroke-width="1"/></svg></div>
  <div class="divider" style="top:771px"></div>

  <h3 class="offer-title" style="left:270px;top:824px">MOBILE WC WAGEN MIETEN</h3>
  <p class="offer-text" style="left:270px;top:852px;width:285px">Sie sind auf der Suche nach einem mobilen WC Container, bzw. Toiletten-container zum mieten? Hier finden Sie unsere mobilen WC Container und WC-Anlagen im Verleih in der Übersicht.</p>
  <div class="details-button" style="left:270px;top:896px">DETAILS<svg width="10" height="10" viewBox="0 0 10 10"><path d="M0 5h9M5 1l4 4-4 4" fill="none" stroke="#2d6db3" stroke-width="1"/></svg></div>
  <div class="product-image product-wagon" role="img" aria-label="Foto eines weißen Toilettenwagens mit blauem Sockel und zwei Treppen"></div>
  <div class="divider" style="top:959px"></div>

  <div class="product-image product-toilet" role="img" aria-label="Foto einer grauen mobilen Toilettenkabine"></div>
  <h3 class="offer-title" style="left:508px;top:1033px">MOBILE WC ANLAGEN KAUFEN</h3>
  <p class="offer-text" style="left:508px;top:1061px">Unsere WC-Kabinen zum mieten bzw im Verleih. Hier finden Sie unsere Toilettenkabinen wie z. B. das mobile Baustellen WC, unser Universal Miete WC oder den Urinalstand in der Übersicht.</p>
  <div class="details-button" style="left:506px;top:1105px">DETAILS<svg width="10" height="10" viewBox="0 0 10 10"><path d="M0 5h9M5 1l4 4-4 4" fill="none" stroke="#2d6db3" stroke-width="1"/></svg></div>
  <div class="divider" style="top:1168px"></div>

  <footer class="site-footer">
    <span>Produkte</span><span>News &amp; Infos</span><span>Unternehmen</span><span>Kontakt</span><span>AGB</span><span>Impressum</span>
  </footer>
</body>
</html>
```